Independent Midwife for a positive birth experience needs a vibrant, and elegant business card/logo

I need a business card design with a logo. The logo I would like to be able to use on my website (www.midwifeorlaith.com) next to my name.
Therefore the design of the card and logo should suit the colours and design of the website. The title of the website and company is "Orlaith Denby Marsworth, Midwife" but I'd like to have the business card title to be "Orlaith Denby Marsworth - Independent Midwife" in bold letters, same script font as in my website.

I provide gold standard midwifery services, one-to-one tailored care, continuity of care throughout the entire pregnancy (antenatal care), the birth and after the birth (postnatal care), home birth, water birth, breast-feeding support, and birth preparation workshops. I also am certified and offer complementary therapies: pregnancy reflexology, rebozo techniques for optimal baby positioning.

The design should incorporate similar colours and style as the website and the "Orlaith Denby Marsworth - Independent Midwife" on the card should include the same font as in the title of the website, however, in bold. The front of the card should have a logo, title and contact information (phone number 071592604, email orlaith.marsworth@quillpost.com, website address www.midwifeorlaith.com).
The back of the card to include the services I offer.

The logo: use of colour purple (varying shades), should communicate communicate warmth, kindness, compassion. It should convey that I'm a midwife who believes in fostering a trusting relationship with my clients and to provide them with a positive pregnancy and birth experience.

Target Market(s)

Pregnant women or women who are looking to book a private midwife for better birth experience and outcome

Industry/Entity Type

Baby

Contact Information for Business Card

Name and Title on front side together with contact details
The reverse side should have services/packages offered

Font styles to use
Script
Other font styles liked:
• similar script as in my website for name and title, and easy to read font for the rest of the words

Colors
b768aa
a54599
d2a4cc
ffffff

Requirements
Must have
• same font as title of website, but slightly bolder.
• similar design, colours, patterns as in website.
• Also include a gold accent colour somewhere in the design please.
Nice to have
• perhaps a logo of pregnant belly in profile or newborn baby icon

```html
<!DOCTYPE html>
<html lang="en">
<head>
<meta charset="utf-8">
<title>Orlaith Denby Marsworth, Independent Midwife – Business Card</title>
<link rel="stylesheet" href="https://fonts.googleapis.com/css2?family=Great+Vibes&family=Lato:wght@300;400&display=swap">
<style>
  :root {
    --lavender: #d2a4cc;
    --lavender-band: #cfa3e6;
    --plum: #b768aa;
    --deep-night: #15101f;
    --shadow-violet: #3a2f52;
    --mist-violet: #8c82a6;
    --white: #ffffff;
    --gold: #d9a53a;
    --gold-deep: #a8782a;
    --logo-lilac: #c68ee0;
    --gap: #ffffff;
  }
  * { box-sizing: border-box; margin: 0; padding: 0; }
  html, body {
    width: 1200px; height: 333px; overflow: hidden;
    background: var(--gap);
  }
  .canvas { position: relative; width: 1200px; height: 333px; }

  .card {
    position: absolute; top: 0; height: 333px; overflow: hidden;
    color: var(--white);
    font-family: "Lato", "Helvetica Neue", Arial, sans-serif;
    font-weight: 300;
  }
  .card--front { left: 0; width: 600px; }
  .card--back { left: 603px; width: 597px; }

  .top-band {
    position: absolute; left: 0; top: 0; right: 0; height: 46px;
    background: var(--lavender-band);
    display: flex; align-items: center; justify-content: space-between;
    padding: 0 16px; font-size: 14px; letter-spacing: 0.2px;
    z-index: 2;
  }

  .photo {
    position: absolute; left: 0; right: 0; top: 46px; bottom: 0;
  }
  .photo--expectant-mother {
    background:
      radial-gradient(ellipse 120px 170px at 355px 140px, rgba(90,80,120,0.55), transparent 70%),
      linear-gradient(90deg, var(--deep-night) 0%, #2a2340 18%, #5a5275 30%, #8a82a8 48%, #3c3356 62%, #6a6290 80%, #2a2340 100%);
  }
  .photo--newborn-hands {
    background:
      radial-gradient(ellipse 180px 120px at 300px 120px, rgba(220,214,235,0.55), transparent 75%),
      radial-gradient(ellipse 260px 160px at 300px 200px, var(--mist-violet), transparent 80%),
      linear-gradient(180deg, var(--shadow-violet) 0%, #4b4466 50%, #221c33 100%);
  }

  .card-title {
    position: absolute; left: 0; right: 0; top: 148px;
    text-align: center;
    font-family: "Great Vibes", "Brush Script MT", cursive;
    font-size: 31px; font-weight: 400; color: var(--white);
    text-shadow: 0 0 1px var(--white);
    z-index: 2;
  }

  .brand {
    position: absolute; left: 14px; bottom: 18px;
    display: flex; align-items: center; gap: 8px;
    z-index: 2;
  }
  .brand__dot {
    width: 22px; height: 22px; border-radius: 50%;
    background: var(--logo-lilac);
  }
  .brand__name {
    font-family: "Lato", "Helvetica Neue", Arial, sans-serif;
    font-weight: 300; font-size: 11px; line-height: 1.3;
    color: var(--logo-lilac); width: 140px;
  }

  .phone {
    position: absolute; right: 20px; bottom: 10px;
    font-size: 19px; font-weight: 400; letter-spacing: 1.5px;
    color: var(--gold); z-index: 2;
  }

  .section-title {
    font-family: "Great Vibes", "Brush Script MT", cursive;
    font-size: 24px; font-weight: 400; justify-content: center;
  }

  .services {
    position: absolute; left: 0; right: 0; top: 67px;
    text-align: center; z-index: 2;
    font-size: 14px; line-height: 19.5px;
  }
  .therapies {
    position: absolute; left: 0; right: 0; top: 208px;
    text-align: center; z-index: 2;
  }
  .therapies__heading { font-size: 17px; font-weight: 400; margin-bottom: 8px; }
  .therapies__list { font-size: 13.5px; }

  .back-url {
    position: absolute; left: 0; right: 0; bottom: 4px;
    text-align: center; font-size: 12px; z-index: 2;
  }

  .seal {
    position: absolute; right: 18px; bottom: 14px;
    width: 58px; height: 58px; z-index: 2;
  }
</style>
</head>
<body>
<main class="canvas">

  <section class="card card--front">
    <header class="top-band">
      <span class="web">www.midwifeorlaith.com</span>
      <span class="email">orlaith.marsworth@quillpost.com</span>
    </header>
    <div class="photo photo--expectant-mother" role="img" aria-label="Monochrome violet-toned photograph of an expectant mother in silhouette by a window, hands on her belly"></div>
    <h1 class="card-title">Orlaith Denby Marsworth, Independent Midwife</h1>
    <div class="brand">
      <span class="brand__dot"></span>
      <span class="brand__name">Orlaith Denby Marsworth, Independent Midwife</span>
    </div>
    <p class="phone">071592604</p>
  </section>

  <section class="card card--back">
    <header class="top-band section-title">Midwife Services</header>
    <div class="photo photo--newborn-hands" role="img" aria-label="Soft violet-toned close-up photograph of a newborn resting in cupped hands"></div>
    <p class="services">
      One-to-one tailored care,<br>
      Continuity of care throughout the entire pregnancy (Antenatal Care),<br>
      The birth and after the birth (Postnantal Care),<br>
      Home birth, Water birth, Breast-feeding support,<br>
      Birth preparation workshop.
    </p>
    <div class="therapies">
      <p class="therapies__heading">Offer Complementary Therapies :</p>
      <p class="therapies__list">Pregnancy reflexologi, Rebozo techniques for optimal bay positioning.</p>
    </div>
    <div class="brand">
      <span class="brand__dot"></span>
      <span class="brand__name">Orlaith Denby Marsworth, Independent Midwife</span>
    </div>
    <svg class="seal" viewBox="0 0 58 58" role="img" aria-label="Certification seal">
      <circle cx="29" cy="29" r="26" fill="var(--gold)" stroke="var(--gold-deep)" stroke-width="2"/>
      <circle cx="29" cy="29" r="18" fill="none" stroke="var(--gold-deep)" stroke-width="1.5"/>
    </svg>
    <p class="back-url">www.midwifeorlaith.com</p>
  </section>

</main>
</body>
</html>
```